ROVA Pty Ltd Business Card

Looking for a simple yet eye-catching double-sided business card design using my company logo on one side and contact details on the other.

Target Market(s)

Government

Industry/Entity Type

Communication Systems Engineering

Contact Information for Business Card

ROVA Pty Ltd

Requirements
Nice to have
• Would be great to have a QR code so details can be scanned into contacts

```html
<!DOCTYPE html>
<html lang="en">
<head>
<meta charset="utf-8">
<title>ROVA Pty Ltd Business Card</title>
<link rel="stylesheet" href="https://fonts.googleapis.com/css2?family=Montserrat:wght@600;700&family=Arimo:wght@400&display=swap">
<style>
  :root {
    --backdrop: #2a2a2a;
    --slate: #36424b;
    --ink: #1f272d;
    --ink-dark: #0b0d0f;
    --paper: #ffffff;
    --rule: #4a4f54;
    --logo-fill: #4a5660;
  }
  * { box-sizing: border-box; margin: 0; padding: 0; }
  html, body {
    width: 1200px; height: 1040px; overflow: hidden;
    background: var(--backdrop);
  }
  .card {
    position: absolute;
    left: 220px;
    width: 760px; height: 434px;
    border-radius: 0 70px 0 70px;
    box-shadow: 0 10px 30px rgba(0,0,0,.45);
  }
  .card--front { top: 60px; background: var(--slate); }
  .card--back  { top: 546px; background: var(--paper); }

  .brand {
    position: absolute;
    display: flex; align-items: center; gap: 26px;
  }
  .brand__mark {
    display: block; width: 110px; height: 130px;
    background: var(--logo-fill); opacity: .35;
  }
  .brand__name {
    font-family: "Montserrat", sans-serif;
    font-weight: 700;
    letter-spacing: 4px;
    line-height: 1;
  }
  .card--front .brand { left: 130px; top: 140px; }
  .card--front .brand__name { font-size: 118px; color: var(--ink-dark); }
  .card--front .brand__mark { width: 150px; height: 160px; }

  .card--back .brand { left: 60px; top: 150px; gap: 22px; }
  .card--back .brand__name { font-size: 64px; color: var(--slate); }
  .card--back .brand__mark { width: 100px; height: 120px; opacity: .2; }

  .divider {
    position: absolute; left: 392px; top: 96px;
    width: 1px; height: 250px; background: var(--rule);
  }
  .contact {
    position: absolute; left: 418px; top: 100px;
    font-family: "Arimo", sans-serif; color: var(--ink);
  }
  .contact__name {
    font-family: "Montserrat", sans-serif; font-weight: 700;
    font-size: 27px; letter-spacing: 1px; line-height: 1.05;
  }
  .contact__role { font-size: 22px; margin-bottom: 14px; }
  .contact__line {
    display: flex; align-items: center; gap: 8px;
    font-size: 24px; line-height: 1.38;
  }
  .contact__line svg { width: 20px; height: 20px; flex: none; }
  .contact__address { font-size: 24px; line-height: 1.25; margin-top: 14px; }
</style>
</head>
<body>
  <section class="card card--front">
    <div class="brand">
      <span class="brand__mark" role="img" aria-label="Company tree emblem area"></span>
      <span class="brand__name">ROVA</span>
    </div>
  </section>

  <section class="card card--back">
    <div class="brand">
      <span class="brand__mark" role="img" aria-label="Company tree emblem area"></span>
      <span class="brand__name">ROVA</span>
    </div>
    <div class="divider"></div>
    <div class="contact">
      <p class="contact__name">JONATHAN SMITH</p>
      <p class="contact__role">Managing Director</p>
      <p class="contact__line">
        <svg viewBox="0 0 24 24" fill="none" stroke="currentColor" stroke-width="2" stroke-linecap="round" stroke-linejoin="round"><path d="M22 16.9v3a2 2 0 0 1-2.2 2 19.8 19.8 0 0 1-8.6-3.1 19.5 19.5 0 0 1-6-6A19.8 19.8 0 0 1 2.1 4.2 2 2 0 0 1 4.1 2h3a2 2 0 0 1 2 1.7c.1.9.4 1.8.7 2.7a2 2 0 0 1-.5 2.1L8 9.8a16 16 0 0 0 6 6l1.3-1.3a2 2 0 0 1 2.1-.4c.9.3 1.8.6 2.7.7a2 2 0 0 1 1.7 2z"/></svg>
        044-123 456 789
      </p>
      <p class="contact__line">
        <svg viewBox="0 0 24 24" fill="none" stroke="currentColor" stroke-width="2"><rect x="2" y="5" width="20" height="14"/><path d="M2 5l10 8 10-8"/></svg>
        info@webname.com
      </p>
      <p class="contact__line">
        <svg viewBox="0 0 24 24" fill="none" stroke="currentColor" stroke-width="2"><circle cx="12" cy="12" r="10"/><path d="M2 12h20M12 2a15 15 0 0 1 0 20M12 2a15 15 0 0 0 0 20"/></svg>
        www.websitename.com
      </p>
      <p class="contact__address">421, Address line goes here<br>45452,Country Name</p>
    </div>
  </section>
</body>
</html>
```